Brightmark Electrical Flyer

An eye catching flyer design which showcases the type of work we do in the electrical industry in Vancouver,BC. The final design should be simple and incorporate our logo. And present a high end company.

Industry/Entity Type

Electrical

```html
<!DOCTYPE html>
<html lang="en">
<head>
<meta charset="utf-8">
<title>Brightmark Electrical Flyer</title>
<link rel="stylesheet" href="https://fonts.googleapis.com/css2?family=PT+Sans:wght@400;700&family=Oswald:wght@500;700&family=Roboto+Condensed:wght@700&display=swap">
<style>
  :root{
    --yellow:#f5d60f;
    --yellow-deep:#eec900;
    --ink:#2a2a2a;
    --grey-text:#4a4a4a;
    --dark-band:#3c3c3c;
    --white:#ffffff;
  }
  *{margin:0;padding:0;box-sizing:border-box;}
  html,body{width:971px;height:1200px;overflow:hidden;background:#fff;}
  .flyer{position:relative;width:971px;height:1200px;background:var(--white);font-family:"PT Sans",sans-serif;color:var(--grey-text);}
  .abs{position:absolute;}

  .brand{left:63px;top:60px;display:flex;align-items:center;gap:16px;}
  .brand-mark{width:44px;height:44px;background:var(--yellow);}
  .brand-name{font-family:"PT Sans",sans-serif;font-weight:700;font-size:54px;color:var(--ink);letter-spacing:1px;line-height:1;}

  .intro{left:63px;top:198px;font-size:23px;line-height:32px;color:var(--grey-text);}

  .feature-band{left:0;top:270px;width:971px;height:401px;background:linear-gradient(90deg,#4a4a4a,#353535 50%,#454545);}
  .about{left:63px;top:289px;width:120px;font-size:20px;line-height:28px;color:#eee;}
  .card{top:292px;width:221px;height:353px;border-radius:46px;overflow:hidden;background:var(--yellow);border:2px solid #fff;text-align:center;color:#222;}
  .card-photo{height:193px;width:100%;}
  .card-title{font-weight:700;font-size:17px;line-height:20px;margin-top:10px;text-transform:uppercase;}
  .card-text{font-size:12.5px;line-height:17px;margin:14px 18px 0;}

  .services{left:0;top:671px;width:971px;height:345px;background:linear-gradient(180deg,#ffffff 0%,#f2f6fa 35%,#dbe6ef 100%);}
  .services-title{left:57px;top:686px;font-family:"Oswald",sans-serif;font-weight:700;font-size:36px;color:var(--yellow-deep);letter-spacing:0.5px;}
  .service-list{list-style:none;font-family:"Roboto Condensed",sans-serif;font-weight:700;font-size:24px;color:#333;}
  .service-list li{height:33px;display:flex;align-items:center;gap:10px;}
  .service-list li::before{content:"";width:18px;height:18px;border-radius:50%;background:radial-gradient(circle at 40% 35%,#fff6a0,var(--yellow) 60%,#c9a800);box-shadow:0 0 0 1px #bbb;}
  .tagline-box{left:659px;top:691px;width:243px;height:191px;background:var(--yellow);border:2px solid #fff;border-radius:8px;box-shadow:0 2px 4px rgba(0,0,0,.25);display:flex;align-items:center;justify-content:center;text-align:center;font-family:"Roboto Condensed",sans-serif;font-weight:700;font-size:27px;line-height:35px;color:#fff;text-shadow:0 1px 2px rgba(0,0,0,.45);}
  .email{left:60px;top:925px;font-size:21px;font-weight:700;color:#111;}
  .website{left:57px;top:962px;font-family:"Roboto Condensed",sans-serif;font-weight:700;font-size:40px;color:var(--ink);}
  .contact-label{left:680px;top:910px;font-family:"Roboto Condensed",sans-serif;font-weight:700;font-size:40px;color:var(--ink);}
  .contact-phone{left:615px;top:956px;font-family:"Roboto Condensed",sans-serif;font-weight:700;font-size:46px;color:var(--ink);}

  .gallery-band{left:0;top:1016px;width:971px;height:163px;background:var(--yellow);}
  .gallery-photo{top:1028px;width:217px;height:137px;border:2px solid #fff;box-shadow:0 2px 4px rgba(0,0,0,.3);}
  .footer-strip{left:0;top:1179px;width:971px;height:21px;background:linear-gradient(90deg,#c9ccd0,#e6e8ea,#c9ccd0);}
</style>
</head>
<body>
<div class="flyer">
  <div class="abs brand"><span class="brand-mark"></span><span class="brand-name">Brightmark Electrical Inc</span></div>
  <p class="abs intro">Brightmark Electrical offers a wide varierty of services, to meet your electrical needs.<br>Whether it may be residential, commercial or industrial.</p>

  <div class="abs feature-band" role="img" aria-label="Dark grey photo of an electrical panel"></div>
  <p class="abs about">We are an electrical contractor serving the lower mainland. Providing the best in customer service and knowledge, to our clients.</p>

  <div class="abs card" style="left:211px">
    <div class="card-photo" role="img" aria-label="Warm lit corridor with feature lighting" style="background:linear-gradient(135deg,#7a1d14,#e0a020 50%,#8a2a10)"></div>
    <h3 class="card-title">Lighting<br>Experts</h3>
    <p class="card-text">We provide all your lighting needs to complete any project from small to large</p>
  </div>
  <div class="abs card" style="left:452px">
    <div class="card-photo" role="img" aria-label="Smart lighting control panel" style="background:linear-gradient(90deg,#d8d2c4,#2a2a2e 35%,#1c1c22 60%,#bfc3c8)"></div>
    <h3 class="card-title">Panelized Smart<br>Lighting</h3>
    <p class="card-text">Smart lighting solutions give you endless options with your lights</p>
  </div>
  <div class="abs card" style="left:694px">
    <div class="card-photo" role="img" aria-label="Electrician with hard hat and tool belt" style="background:linear-gradient(160deg,#b7343a,#f2d21a 45%,#c49a4a 75%,#7a5a3a)"></div>
    <h3 class="card-title">Quality on Time<br>Construction</h3>
    <p class="card-text" style="font-size:12px;line-height:17px">We efficiently manage construction and co odinate with schedules to always give our clients an effortless experience.</p>
  </div>

  <div class="abs services" role="img" aria-label="Bright modern hall interior"></div>
  <h2 class="abs services-title">TYPES OF SERVICES</h2>
  <ul class="abs service-list" style="left:66px;top:738px">
    <li>RESIDENTIAL</li><li>INDUSTRIAL</li><li>FIRE ALARM</li><li>SOLAR PANEL</li><li>VOLTAGE WIRING</li>
  </ul>
  <ul class="abs service-list" style="left:287px;top:738px">
    <li>COMMERICAL</li><li>LIGHTING</li><li>SECURITY</li><li>LOW</li>
  </ul>
  <div class="abs tagline-box">RESIDENTIAL<br>COMMERCIAL<br>AND INDUSTRIAL<br>ELECTRICAL<br>SERVICES</div>
  <p class="abs email">Email: info@brightmarkelectrical.ca</p>
  <p class="abs website">www.brightmarkelectrical.ca</p>
  <p class="abs contact-label">CONTACT US</p>
  <p class="abs contact-phone">778 555 0142</p>

  <div class="abs gallery-band"></div>
  <div class="abs gallery-photo" style="left:33px;background:linear-gradient(180deg,#8fb8e0,#b5563a 55%,#6a8a4a)" role="img" aria-label="Brick townhouses"></div>
  <div class="abs gallery-photo" style="left:258px;background:linear-gradient(180deg,#3a4a6a,#d8c0a0 55%,#3f6a8a)" role="img" aria-label="Modern house with lit pool at dusk"></div>
  <div class="abs gallery-photo" style="left:483px;background:linear-gradient(180deg,#f0ede4,#e0dcd0 50%,#d9702a)" role="img" aria-label="Office lounge with orange chairs"></div>
  <div class="abs gallery-photo" style="left:708px;background:linear-gradient(180deg,#cfe0ec,#8fb0c8 55%,#e8eef2)" role="img" aria-label="Bright shopping mall interior"></div>
  <div class="abs footer-strip"></div>
</div>
</body>
</html>
```